Leadership/Education Book Cover Project

I need a book cover design for a new book titled "Purposeful Inclusion Stewardship: Sparking Renewal and Reform across Tertiary Schooling."

This book is written to be a Tide Turner! Hence I need a game changing design!

The focus of the book is to help colleges and universities to build sustainable capacity to become more diverse (race, ethnicity, nationality, gender, sexual orientation), embrace diversity, and prepare all students irrespective of background for a world that is diverse, global, and interconnected.

I am looking for an "elegant" highly professional design that is directed towards leaders of organizations. Presidents, chief diversity officers, vice presidents, faculty - the goal is for the design to sell concepts like - professional, leadership, strategic, clear, organizational change management, planning, focus, discipline, etc - these are the lead themes - diversity is the issue, but I need to position this as an organizational change, management book for higher education audiences.

Less is more - as I am most looking for a typographic design theme, more than an image based design. At the same time, I am not opposed to having a design that includes some type of graphic elements that capture the key ideas.

No typical "diversity images" like hands, rainbows, etc. It has to be more sophisticated than that if your going to use images - also no people. No smiling multicultural faces. This is a business, management, leadership book - that is meant to be the definitive contribution of it's kind. Some models might include - Tide Turner, Fair Toward Fine, 17 Rules of Stewardship, Flint, Stragglers, A Horizon for Oversight, Racing Toward Tomorrow, Steering the Upheaval, and Those Stalled Campuses.

At the same time, don't feel limited to these exact executions. I am open to some exploration of possibilities.

My color - taste is open, but the key is professional colors - nothing outlandish - nothing to bold. More subdued - as I am trying to find an image that suggests this is the best, most trust - worthy book ever written that can help you to manage your strategic diversity issues of access, inclusion, learning, etc - this book can help you to be more relevant and vibrant in the 21st Century Knowledge Economy.

If you use images - go deep into the concepts I offer here - don't live a the surface of the word diversity.

Here is some additional information about the book:

A Question of Merit: Purposeful Inclusion Stewardship in the Campus
By
Dr. Harlan T. Brooksby & Dr. Lorelle P. Mintz-Harrow
Quarrel Lane Press
Anticipated Publication January 2012

This book, Purposeful Inclusion Stewardship: Sparking Renewal and Reform across Tertiary Schooling focuses squarely on the topic of managing diversity in a higher education context. In doing this, it challenges the higher education community and others, to face what Ned Farrow, noted author of the book on excellence, Fair Toward Fine, refers to as the brutal facts of their reality. Namely, that diversity is no longer simply a question of moral and social responsibility, but a matter of excellence. A matter of enhancing organizational creativity, learning, problem solving, and institutional effectiveness - - a matter of sustainability and maintaining global competitiveness in a 21st Century global knowledge economy.

Over the past century, American higher education has evolved dramatically. Once a privilege reserved for the elite, it has become a requirement for the majority. No longer the ivory tower, colleges and universities must be catalysts of economic development, laboratories for big ideas, and incubators of diverse leaders who champion the promise of American Democracy in the new economy. An economy where computer geeks rule and innovation eats orthodoxy, higher education is the key to our present and our future.

Issues of access, equity, and inclusion, matters of diversity must live in the foreground of institutional life. Nearly every great national challenge — from the search for clean energy, to the need for a new generation of scientists, depends on higher education and the benefits of diversity. Computer labs and internet workspaces are what assembly lines and automotive plants were 100 years ago-the drivers of growth in both good and bad times. Spaces where people must come together, collaborate, and harness the power of difference towards creative goals in a fast past and changing world.
A New Vision for Higher Education

Changing demographics, the emergence of a knowledge-based economy, chronic social inequities, a focus on the educational benefits of diverse learning environments, and workforce demands for graduates prepared to lead and follow in a global and interconnected world mandates a new approach to issues of diversity. An approach where our efforts are grounded in empirical evidence and best-practice efforts to achieve changes that are more than symbolic. Change that is not held hostage by personal anecdotes and the whims of leaders who have little experience with matters of institutional transformation, and even less experience leading these conversations around matters of diversity.

Now more than ever before, educational leaders need to ask themselves what are the big picture 21st century issues of diversity? What dynamics both constrain and enable our diversity agenda? In fact, how do we define diversity in the new millennium? Why was our diversity plan less than successful? What strategies do we have in place to advance diversity issues on campus? Are we at threat of being sued? Is diversity operating at a high enough level on campus? How should we track and define diversity in the new millennium? Do we need a chief diversity officer? If so, at what level of rank? Who should they supervise? Is diversity consistently on our agenda in the president’s cabinet, on the floor of faculty senate, or in the various school, college and divisional departments that exist across campus? Are we our own worse enemy? These are questions that institutional leaders have to ask themselves. To do anything less, is to simply throw money at a problem, or replay the same broken record without any new actions designed to break the cycle of failure, exclusion, and deprivation, echoing the clinical definition of insanity – repeating the same actions over and over again, expecting a new result!

In the world we live in today, diversity is not just the right thing to do- - it is the only thing to do. More than anecdotes and lived experiences, this book delivers theoretical and empirically grounded advice for institutions attempting to enhance their strategic capabilities by developing, optimizing, and better understanding the various diversity efforts that exist at their schools. Indeed in this book, we spend an entire chapter, embracing the complexity and challenge of defining diversity in a world in which race, ethnicity, gender, sexuality, nationality, and a host of other identities are all potentially tantamount to an institution’s definition and activation of the diversity idea on campuses big and small, rural and urban, private and public.

Not just a book for Chief Diversity Officers (CDO) or diversity professionals, this book is intended for ‘diversity champions’ who want to become strategic diversity leaders in the academy. A term we use to broadly refer to anyone involved in facilitating, initiating, influencing, or implementing diversity themed projects, or initiatives, whether or not they have an official title recognizing that responsibility or not. More than a how-to guide, this book is about both the process of leading diversity themed change, as well as the nature of diversity themed change in the academy. It presents a range of models, strategies, and contingencies that must be considered whether the goal is developing a rationale for campus diversity, building a new chief diversity officer role, reorganizing the current campus diversity infrastructure, developing a new diversity plan, defining diversity, or assessing the diversity process and journey of change. As a result, it has utility for anyone, regardless of role, who is interested in the process of strategic diversity leadership.
Updates

Book should be "single author" - Dr. Harlan T. Brooksby

Designers -

I have posted some additional information that may enhance "text" driven design concepts.  It's information for using wordle - to generate concepts.  I have included:

(1) PIS - text for drop into wordle
(2) PIS - guide to give you settings for wordle
(3) Wordle - example of a pdf I like

You can feel free to use these to generate/revise concepts.  All other aspects of the brief still hold.

HTB

Reason: Designers - my apologies - I had a family situation - and was totally out of commission - I appreciate your patience - and plan to move forward.

The book will ultimately be 6 x 9 inches

htb

Target Market(s)

College and university presidents, senior leaders in higher education, faculty, chief diversity officers, business leaders - professionals

Industry/Entity Type

Sustainability

Requirements
Must have
• The book must have the full title:

Purposeful Inclusion Stewardship:
Sparking Renewal and Reform across Tertiary Schooling

Author:
Harlan T. Brooksby, PhD
Should not have
• No - obvious diversity references - hands, globes, diverse people, rainbows, etc - the focus is on "strategic diversity leadership" attempting to usher in a bold new paradigm centered on the idea that issues of diversity, equity, and inclusion - are key to the economic viability of the nation in a new global knowledge economy. That it's only being intentional in our efforts, to embrace diverse people, ideas, perspectives, etc - that we can become stronger as a nation.

```html
<!DOCTYPE html>
<html lang="en">
<head>
<meta charset="utf-8">
<title>Purposeful Inclusion Stewardship — Book Cover</title>
<link href="https://fonts.googleapis.com/css2?family=Alegreya:wght@400&family=Roboto+Condensed:wght@700&display=swap" rel="stylesheet">
<style>
  :root {
    --page: #ffffff;
    --ink: #231f20;
    --accent-green: #1ba77f;
    --deep-blue: #0d4a6b;
    --author-blue: #14507a;
    --edge: #3a3a3a;
  }
  html, body {
    margin: 0;
    width: 1200px;
    height: 900px;
    overflow: hidden;
    background: var(--page);
  }
  .canvas {
    position: relative;
    width: 1200px;
    height: 900px;
  }
  .cover {
    position: absolute;
    left: 313px;
    top: 42px;
    width: 592px;
    height: 818px;
    background: var(--page);
    border: 1px solid var(--edge);
    box-sizing: border-box;
    box-shadow: 2px 3px 4px rgba(0,0,0,0.22);
    overflow: hidden;
  }
  .artwork-area {
    position: absolute;
    left: 0;
    top: 0;
  }
  .title-block {
    position: absolute;
    left: 0;
    width: 100%;
    top: 290px;
    text-align: center;
    font-family: "Alegreya", Georgia, serif;
    color: var(--ink);
  }
  .title-upper {
    margin: 0;
    font-size: 40px;
    font-weight: 400;
    letter-spacing: 3.5px;
    line-height: 1;
    padding-top: 7px;
  }
  .title-main {
    margin: 0;
    font-size: 74px;
    font-weight: 400;
    letter-spacing: 3px;
    line-height: 1;
    margin-top: 12px;
  }
  .subtitle {
    margin: 14px 0 0;
    font-size: 19px;
    color: var(--accent-green);
    letter-spacing: 0.2px;
  }
  .author {
    position: absolute;
    right: 46px;
    top: 752px;
    margin: 0;
    font-family: "Roboto Condensed", "Arial Narrow", sans-serif;
    font-weight: 700;
    font-size: 17px;
    letter-spacing: 1.6px;
    color: var(--author-blue);
  }
</style>
</head>
<body>
<div class="canvas">
  <div class="cover">
    <svg class="artwork-area" width="592" height="818" viewBox="313 42 592 818" role="img" aria-label="Cover artwork area: a large half-round graphic in green and deep blue tones framing the title">
      <defs>
        <linearGradient id="artwork-tone" gradientUnits="userSpaceOnUse" x1="0" y1="42" x2="0" y2="860">
          <stop offset="0" stop-color="#1c9d7c"/>
          <stop offset="0.3" stop-color="#0d4a6b"/>
          <stop offset="0.62" stop-color="#0d4a6b"/>
          <stop offset="1" stop-color="#1bb07f"/>
        </linearGradient>
        <clipPath id="half-round">
          <circle cx="349" cy="420" r="431"/>
        </clipPath>
      </defs>
      <g fill="url(#artwork-tone)" clip-path="url(#half-round)">
        <rect x="313" y="42" width="460" height="270"/>
        <rect x="313" y="527" width="460" height="333"/>
      </g>
    </svg>

    <div class="title-block">
      <h1 class="title-upper">PURPOSEFUL INCLUSION</h1>
      <p class="title-main">STEWARDSHIP</p>
      <p class="subtitle">Sparking Renewal &amp; Reform across Tertiary Schooling</p>
    </div>

    <p class="author">HARLAN T. BROOKSBY, PHD</p>
  </div>
</div>
</body>
</html>
```